Corvane Supplies Business Card

Professional business card that stand out to our potential customers. Front and back with clean modern design

Industry/Entity Type

Oil and gas

Contact Information for Business Card

Name, address, website , office phone and cell number

Requirements
Must have
• Editable files for each employee

```html
<!DOCTYPE html>
<html lang="en">
<head>
<meta charset="utf-8">
<title>Corvane Supplies — Business Card</title>
<link href="https://fonts.googleapis.com/css2?family=Michroma&family=Arimo:wght@400;700&display=swap" rel="stylesheet">
<style>
  :root {
    --red: #ff0000;
    --cyan: #06b2d2;
    --ink: #111111;
    --paper: #ffffff;
    --stage: #c4c4c4;
    --mid: #7a5566;
  }
  * { box-sizing: border-box; margin: 0; padding: 0; }
  html, body { width: 1200px; height: 800px; overflow: hidden; }
  body {
    background: var(--stage);
    font-family: "Arimo", Arial, sans-serif;
    position: relative;
  }
  .card {
    position: absolute;
    width: 540px;
    height: 310px;
    border-radius: 18px;
    overflow: hidden;
    box-shadow: 0 14px 30px rgba(0,0,0,0.25);
  }
  /* Front */
  .card-front { left: 330px; top: 60px; background: var(--paper); }
  .holder-name {
    position: absolute; left: 34px; top: 72px;
    font-family: "Michroma", sans-serif; font-size: 19px; font-weight: 400; letter-spacing: 1px;
    text-transform: uppercase; color: var(--red); white-space: nowrap;
  }
  .holder-name .surname { color: var(--cyan); }
  .contact-band {
    position: absolute; left: 0; top: 140px; width: 300px; height: 78px;
    background: var(--red);
    padding: 10px 0 0 34px;
    color: var(--paper); font-size: 14px; line-height: 19px;
  }
  .contact-band li { list-style: none; display: flex; align-items: center; gap: 8px; white-space: nowrap; }
  .contact-band svg { width: 13px; height: 13px; flex: none; }
  .address {
    position: absolute; left: 34px; top: 238px;
    color: var(--ink); font-size: 15px; line-height: 20px; font-style: normal;
  }
  .accent-band {
    position: absolute; right: 0; top: 60px; width: 150px; height: 52px;
    background: var(--cyan);
  }
  .front-brand {
    position: absolute; left: 320px; top: 150px; width: 200px;
    display: flex; align-items: center; gap: 10px;
    font-family: "Michroma", sans-serif; font-size: 15px; line-height: 22px;
    text-transform: uppercase; color: var(--red);
  }
  .front-brand .mark { width: 18px; height: 18px; background: var(--red); flex: none; }
  /* Back */
  .card-back {
    left: 330px; top: 430px;
    background: linear-gradient(30deg, var(--red) 0%, #c8252f 35%, var(--mid) 58%, #2a9bb8 78%, var(--cyan) 100%);
    display: flex; align-items: center; justify-content: center;
  }
  .back-brand {
    display: flex; align-items: center; gap: 14px;
    font-family: "Michroma", sans-serif; font-size: 24px; letter-spacing: 1px;
    text-transform: uppercase; color: var(--paper); white-space: nowrap;
  }
  .back-brand .mark { width: 22px; height: 22px; background: var(--paper); flex: none; }
</style>
</head>
<body>
  <section class="card card-front" aria-label="Business card front">
    <h1 class="holder-name">Dorian <span class="surname">Hale</span></h1>
    <ul class="contact-band">
      <li>
        <svg viewBox="0 0 16 16" fill="none" stroke="currentColor" stroke-width="1.6"><path d="M3 2h3l1.5 3.5-2 1.5a8 8 0 0 0 3.5 3.5l1.5-2L14 10v3a1 1 0 0 1-1 1A12 12 0 0 1 2 3a1 1 0 0 1 1-1z"/></svg>
        055-310 482 716
      </li>
      <li>
        <svg viewBox="0 0 16 16" fill="none" stroke="currentColor" stroke-width="1.6"><rect x="4" y="1.5" width="8" height="13" rx="1.5"/><path d="M7 12.5h2"/></svg>
        055-310 482 907
      </li>
      <li>
        <svg viewBox="0 0 16 16" fill="none" stroke="currentColor" stroke-width="1.4"><circle cx="8" cy="8" r="6.3"/><path d="M1.7 8h12.6M8 1.7c2.2 2.2 2.2 10.4 0 12.6M8 1.7c-2.2 2.2-2.2 10.4 0 12.6"/></svg>
        www.corvanesupply.com
      </li>
    </ul>
    <address class="address">
      18 Basin Road, Suite 4<br>67210, Harlow Flats
    </address>
    <div class="accent-band"></div>
    <div class="front-brand"><span class="mark"></span><span>Corvane Supplies</span></div>
  </section>

  <section class="card card-back" aria-label="Business card back">
    <div class="back-brand"><span class="mark"></span><span>Corvane Supplies</span></div>
  </section>
</body>
</html>
```